Lower-middle market private equity firm needs its PowerPoint template update/refresh

Wexford Lindqvist Capital Partners is a lower-middle market private equity firm focused on acquiring family- and founder-owned businesses in the industrial market. Website is here for more info: https://www.wlcpx-example.com/. We would like to upgrade/update our powerpoint template/slide master we use for marketing materials - uploading a powerpoint version with some of the slide templates we use. We would like to keep it classic and clean with a white background and color on top and enough room for text on the pages. We would prefer to stay within the color palette of the hash tag logo on the cover page (cover page needs an update as well). We are open to suggestions on the font we utilize as well.

```html
<!DOCTYPE html>
<html lang="en">
<head>
<meta charset="utf-8">
<title>Wexford Lindqvist Capital Partners – Slide Template</title>
<link href="https://fonts.googleapis.com/css2?family=Archivo:wght@600;700;800;900&family=Inter:wght@400;500;600;700&display=swap" rel="stylesheet">
<style>
  :root{
    --board:#1b1b1b;
    --blue:#2c5f99;
    --blue-deep:#234d80;
    --olive:#a59a2b;
    --green:#4e9a3f;
    --sky:#6fb3e0;
    --periwinkle:#7f9ccc;
    --ink:#444a52;
    --muted:#5a5f66;
    --white:#ffffff;
    --cream:#f1eee0;
  }
  *{margin:0;padding:0;box-sizing:border-box}
  html,body{width:1029px;height:1200px;overflow:hidden;background:var(--board)}
  body{position:relative;font-family:"Inter",sans-serif;color:var(--ink)}
  .slide{position:absolute;width:458px;height:257px;background:var(--white);overflow:hidden}
  .slide::after{content:"";position:absolute;left:0;right:0;bottom:0;height:2px;background:var(--blue)}
  .slide.no-rule::after{display:none}
  .col-l{left:39px}.col-r{left:533px}
  .row-1{top:41px}.row-2{top:328px}.row-3{top:614px}.row-4{top:901px}

  /* header */
  .mark{position:absolute;left:26px;top:13px;width:18px;height:18px;background:var(--blue)}
  .kicker{position:absolute;left:60px;top:10px;font-size:6px;color:var(--muted)}
  .title{position:absolute;left:60px;top:17px;font-family:"Archivo",sans-serif;font-weight:800;font-size:14px;color:var(--blue);letter-spacing:.1px}

  /* cover */
  .cover{background:var(--blue)}
  .cover .photo{position:absolute;inset:0}
  .brand{position:absolute;left:23px;top:37px;font-family:"Archivo",sans-serif;font-weight:800;color:var(--white);line-height:.98}
  .brand .l1,.brand .l2{display:block;font-size:16.5px;letter-spacing:.2px}
  .brand .l3{display:block;font-size:9.4px;margin-top:2px;letter-spacing:.1px}
  .cover h1{position:absolute;left:23px;top:148px;font-family:"Archivo",sans-serif;font-weight:800;font-size:21px;line-height:1.03;color:var(--white);letter-spacing:.3px}
  .cover .tag{position:absolute;left:22px;top:195px;font-family:"Archivo",sans-serif;font-weight:700;font-size:7.4px;color:var(--white);letter-spacing:.2px}
  .cover .web{position:absolute;left:23px;top:217px;width:144px;height:22px;background:var(--white);clip-path:polygon(6px 0,100% 0,calc(100% - 6px) 100%,0 100%);display:flex;align-items:center;justify-content:center;font-family:"Archivo",sans-serif;font-weight:700;font-size:6.6px;color:var(--blue)}

  /* mission */
  .lead{position:absolute;left:40px;right:40px;text-align:center;font-size:7.2px;line-height:12px;color:var(--ink)}
  .pillar{position:absolute;width:92px;text-align:center}
  .pillar h3{font-family:"Archivo",sans-serif;font-weight:700;font-size:6px;letter-spacing:.2px;margin-bottom:4px}
  .pillar p{font-size:5.1px;line-height:8.6px;color:var(--ink)}
  .dia{position:absolute;width:47px;height:47px}
  .dia .sq{position:absolute;left:7px;top:7px;width:33px;height:33px;transform:rotate(45deg);box-shadow:1px 2px 4px rgba(0,0,0,.25)}
  .dia svg{position:absolute;left:13px;top:13px;width:21px;height:21px}
  .c-olive{color:var(--olive)}.c-blue{color:var(--blue)}.c-green{color:var(--green)}.c-peri{color:var(--periwinkle)}.c-sky{color:var(--sky)}
  .b-olive{background:var(--olive)}.b-blue{background:var(--blue)}.b-green{background:var(--green)}.b-peri{background:var(--periwinkle)}.b-sky{background:var(--sky)}

  /* who we are */
  .body-copy{position:absolute;left:229px;top:59px;width:205px;font-size:6px;line-height:11.5px;text-align:justify;color:var(--ink)}
  .body-copy p+p{margin-top:11.5px}
  .art{position:absolute}

  /* why choose us */
  .mini{position:absolute;width:37px;height:37px}
  .mini .sq{position:absolute;left:5.5px;top:5.5px;width:26px;height:26px;transform:rotate(45deg);border:1.5px solid var(--white);box-shadow:1px 2px 4px rgba(0,0,0,.22)}
  .mini svg{position:absolute;left:10px;top:10px;width:17px;height:17px}
  .point{position:absolute;width:74px}
  .point.left{text-align:right}
  .point h4{font-family:"Archivo",sans-serif;font-weight:600;font-size:5.3px;letter-spacing:.15px;margin-bottom:2px}
  .point p{font-size:4.3px;line-height:7px;color:var(--ink)}

  /* table */
  .intro{position:absolute;left:40px;right:40px;top:42px;text-align:center;font-size:6.9px;line-height:11px;color:var(--ink)}
  .table{position:absolute;left:121px;top:76px;width:216px;height:165px;border:1px solid var(--olive);border-radius:12px;overflow:hidden;box-shadow:0 3px 10px rgba(0,0,0,.12);background:var(--white)}
  .table .head{height:23px;background:var(--olive);display:flex;align-items:center;font-family:"Archivo",sans-serif;font-weight:700;font-size:6.6px;color:var(--white);letter-spacing:.2px}
  .table .head span:first-child{margin-left:18px}
  .table .head span:last-child{position:absolute;left:168px}
  .table ol{list-style:none;margin-top:10px}
  .table li{position:relative;height:18.1px;font-size:6.5px;color:var(--ink);line-height:18.1px}
  .table li .n{position:absolute;left:18px}
  .table li .f{position:absolute;left:36px}
  .table li .v{position:absolute;left:168px;font-weight:600}

  /* pills */
  .pill{position:absolute;left:93px;width:272px;height:27px;border-radius:14px;background:linear-gradient(90deg,var(--cream),#fbfaf5 55%,var(--white));border:1px solid #e8e5d6;box-shadow:0 1px 3px rgba(0,0,0,.08);font-size:7px;line-height:25px;padding-left:13px;color:var(--ink)}
  .pill .num{position:absolute;left:251px;top:6px;width:14px;height:14px;border-radius:50%;background:var(--olive);color:var(--white);font-family:"Archivo",sans-serif;font-weight:700;font-size:5.5px;line-height:14px;text-align:center}

  /* thank you */
  .closing .scene{position:absolute;inset:0;background:linear-gradient(120deg,#12263d 0%,#1d3550 40%,#3a2c22 75%,#6a4d30 100%)}
  .closing .panel{position:absolute;left:60px;top:41px;width:336px;height:176px;border-radius:12px;background:rgba(44,95,153,.86);text-align:center;color:var(--white)}
  .closing h2{margin-top:24px;font-family:"Archivo",sans-serif;font-weight:800;font-size:16px;line-height:18.5px;letter-spacing:.3px}
  .closing .sub{margin-top:5px;font-size:6.4px;font-weight:600}
  .closing .txt{margin:6px auto 0;width:236px;font-size:5.9px;line-height:11.5px}
  .closing .txt+.txt{margin-top:11px}
</style>
</head>
<body>

<!-- Cover -->
<section class="slide cover col-l row-1">
  <svg class="photo" viewBox="0 0 458 257" width="458" height="257">
    <defs>
      <linearGradient id="warehouse" x1="0" y1="0" x2="1" y2="1">
        <stop offset="0" stop-color="#0e1a2e"/>
        <stop offset=".45" stop-color="#5a3a22"/>
        <stop offset=".7" stop-color="#23406a"/>
        <stop offset="1" stop-color="#0b1424"/>
      </linearGradient>
    </defs>
    <polygon points="231,0 458,0 458,257 162,257" fill="url(#warehouse)" role="img" aria-label="Photo of an illuminated automated warehouse with stacked cargo shelving"/>
    <polygon points="228,127 232,257 156,257" fill="var(--olive)"/>
  </svg>
  <div class="brand"><span class="l1">WEXFORD</span><span class="l2">LINDQVIST</span><span class="l3">CAPITAL PARTNERS</span></div>
  <h1>REALIZING<br>THE PROMISE</h1>
  <div class="tag">IN SMALL COMPANIES FOR DECADES</div>
  <div class="web">WEBSITE: WWW.WLCPX-EXAMPLE.COM</div>
</section>

<!-- What makes us unique -->
<section class="slide col-r row-1">
  <div class="mark"></div>
  <div class="kicker">What Makes Us Unique</div>
  <div class="title">EXPERIENCE. INTEGRITY. RESULTS.</div>
  <p class="lead" style="top:45px">Our mission is to partner with management teams to achieve new levels of growth<br>and development.</p>

  <div class="dia" style="left:46px;top:79px"><div class="sq b-olive"></div>
    <svg viewBox="0 0 24 24" fill="none" stroke="#fff" stroke-width="1.3"><circle cx="12" cy="13" r="8"/><circle cx="12" cy="11" r="2.6"/><path d="M7.5 18c1-2.5 3-3.5 4.5-3.5s3.5 1 4.5 3.5"/></svg></div>
  <div class="pillar" style="left:24px;top:136px"><h3 class="c-olive">EXPERIENCE</h3><p>Non numquam eius modi tempora incidunt ut labore et dolore magn am aliquam quaerat voluptatem. Ut enim ad minima</p></div>

  <div class="dia" style="left:152px;top:110px"><div class="sq b-blue"></div>
    <svg viewBox="0 0 24 24" fill="none" stroke="#fff" stroke-width="1.3"><circle cx="12" cy="12" r="3"/><circle cx="12" cy="12" r="7" stroke-dasharray="3 2"/></svg></div>
  <div class="pillar" style="left:130px;top:167px"><h3 class="c-blue">INTEGRITY</h3><p>Non numquam eius modi tempora incidunt ut labore et dolore magn am aliquam quaerat voluptatem. Ut enim ad minima</p></div>

  <div class="dia" style="left:259px;top:88px"><div class="sq b-green"></div>
    <svg viewBox="0 0 24 24" fill="none" stroke="#fff" stroke-width="1.3"><path d="M5 18v-4M8.5 18v-6M12 18v-8"/><circle cx="16" cy="13" r="3"/><path d="M18.2 15.2l2.3 2.3"/><path d="M4 19h16"/></svg></div>
  <div class="pillar" style="left:236px;top:145px"><h3 class="c-green">RESULTS</h3><p>Non numquam eius modi tempora incidunt ut labore et dolore magn am aliquam quaerat voluptatem. Ut enim ad minima</p></div>

  <div class="dia" style="left:365px;top:110px"><div class="sq b-peri"></div>
    <svg viewBox="0 0 24 24" fill="none" stroke="#fff" stroke-width="1.3"><path d="M4 13l4-3 4 2 4-2 4 3-6 5z"/><path d="M9 6l.6 1.2 1.3.2-1 .9.3 1.3-1.2-.7M15 6l.6 1.2 1.3.2-1 .9.3 1.3-1.2-.7"/></svg></div>
  <div class="pillar" style="left:343px;top:167px"><h3 class="c-peri">PARTNERSHIPS</h3><p>Non numquam eius modi tempora incidunt ut labore et dolore magn am aliquam quaerat voluptatem. Ut enim ad minima</p></div>
</section>

<!-- Who we are -->
<section class="slide col-l row-2">
  <div class="mark"></div>
  <div class="kicker">Our Firm</div>
  <div class="title">WHO WE ARE</div>
  <svg class="art" style="left:22px;top:54px" width="186" height="180" viewBox="0 0 186 180">
    <defs>
      <linearGradient id="team" x1="0" y1="0" x2="1" y2="1">
        <stop offset="0" stop-color="#a59a2b"/>
        <stop offset=".35" stop-color="#6fb3e0"/>
        <stop offset=".65" stop-color="#8a6a4e"/>
        <stop offset="1" stop-color="#4e9a3f"/>
      </linearGradient>
    </defs>
    <polygon points="93,0 186,90 93,180 0,90" fill="url(#team)" role="img" aria-label="Photo of a smiling businesswoman shaking hands across a desk, framed by coloured diamond tiles"/>
  </svg>
  <div class="body-copy">
    <p>We seek entrepreneur and family-owned companies or corporate divestitures that have a dominant position in their niche sub-sectors of B2B services, distribution and highly engineered manufacturing. Companies with revenues of $15 – $200 million and earnings of $3 – $15 million located in the U.S. and Canada.</p>
    <p>Partnerships with our management teams create multiple paths of value creation. We value people and build strong relationships. We are engaged owners, but not day-to-day operators creating a culture of collaboration and providing strategic resources and guidance to support our management teams.</p>
    <p>Investments across our past three funds map into the investment themes below. We believe these themes underpin secular tailwinds to drive customer demand.</p>
  </div>
</section>

<!-- Master slide -->
<section class="slide col-r row-2">
  <div class="mark"></div>
  <div class="kicker">Title</div>
  <div class="title">MASTER SLIDE</div>
</section>

<!-- Why choose us -->
<section class="slide col-l row-3">
  <div class="mark"></div>
  <div class="kicker">Our Firm</div>
  <div class="title">WHY CHOOSE US</div>
  <svg class="art" style="left:141px;top:54px" width="176" height="178" viewBox="0 0 176 178">
    <defs>
      <linearGradient id="weave" x1="0" y1="0" x2="1" y2="1">
        <stop offset="0" stop-color="#a59a2b"/>
        <stop offset=".3" stop-color="#4e9a3f"/>
        <stop offset=".55" stop-color="#6fb3e0"/>
        <stop offset=".8" stop-color="#7f9ccc"/>
        <stop offset="1" stop-color="#4e9a3f"/>
      </linearGradient>
    </defs>
    <polygon points="88,0 176,89 88,178 0,89" fill="url(#weave)" role="img" aria-label="Interwoven diamond bands filled with financial and network imagery"/>
  </svg>

  <div class="point left" style="left:10px;top:86px"><h4 class="c-green">STRATEGIC FOCUS</h4><p>We seek entrepreneur and family-owned companies or corporate divestitures that have a dominant position</p></div>
  <div class="mini" style="left:94px;top:78px"><div class="sq b-green"></div>
    <svg viewBox="0 0 24 24" fill="none" stroke="#fff" stroke-width="1.4"><circle cx="12" cy="10" r="5"/><circle cx="12" cy="10" r="1.6"/><path d="M9 15l-1 5 4-2 4 2-1-5"/></svg></div>

  <div class="point" style="left:375px;top:86px"><h4 class="c-peri">INVESTMENT THEMES</h4><p>We believe these themes underpin secular tailwinds to drive customer demand.</p></div>
  <div class="mini" style="left:326px;top:78px"><div class="sq b-peri"></div>
    <svg viewBox="0 0 24 24" fill="none" stroke="#fff" stroke-width="1.4"><circle cx="12" cy="12" r="7"/><path d="M12 8v8M10 10h3a1.5 1.5 0 010 3h-2a1.5 1.5 0 000 3h3"/></svg></div>

  <div class="point left" style="left:10px;top:178px"><h4 class="c-sky">VALUE-ADDED APPROACH</h4><p>Partnerships with our management teams create multiple paths of value creation.</p></div>
  <div class="mini" style="left:94px;top:170px"><div class="sq b-sky"></div>
    <svg viewBox="0 0 24 24" fill="none" stroke="#fff" stroke-width="1.4"><circle cx="7" cy="7" r="2"/><circle cx="17" cy="17" r="2"/><path d="M9 7h6a3 3 0 010 6H9a3 3 0 000 6h6"/></svg></div>

  <div class="point" style="left:375px;top:178px"><h4 class="c-olive">INVESTMENT CRITERIA</h4><p>We target companies that benefit from many of the leading trends impacting modern industrial markets</p></div>
  <div class="mini" style="left:326px;top:170px"><div class="sq b-olive"></div>
    <svg viewBox="0 0 24 24" fill="none" stroke="#fff" stroke-width="1.4"><circle cx="11" cy="11" r="6"/><path d="M11 5v6h6"/><circle cx="17" cy="17" r="3"/></svg></div>
</section>

<!-- Investment criteria table -->
<section class="slide col-r row-3">
  <div class="mark"></div>
  <div class="kicker">Our Features</div>
  <div class="title">INVESTMENT CRITERIA</div>
  <p class="intro">Quia non numquam eius modi tempora incidunt ut labore et dolore magnam<br>aliquam quaerat voluptatem. Ut enim ad minima veniam</p>
  <div class="table">
    <div class="head"><span>FEATURES</span><span>VALUE</span></div>
    <ol>
      <li><span class="n">1)</span><span class="f">Transactions Completed</span><span class="v">$2B+</span></li>
      <li><span class="n">2)</span><span class="f">Companies Acquired</span><span class="v">80+</span></li>
      <li><span class="n">3)</span><span class="f">Management Shareholders</span><span class="v">500+</span></li>
      <li><span class="n">4)</span><span class="f">Years of Experience</span><span class="v">40+</span></li>
      <li><span class="n">5)</span><span class="f">Transactions Completed</span><span class="v">$2B+</span></li>
      <li><span class="n">6)</span><span class="f">Management Shareholders</span><span class="v">500+</span></li>
      <li><span class="n">7)</span><span class="f">Companies Acquired</span><span class="v">80+</span></li>
    </ol>
  </div>
</section>

<!-- Our investment criteria -->
<section class="slide col-l row-4">
  <div class="mark"></div>
  <div class="kicker">Why Us</div>
  <div class="title">OUR INVESTMENT CRITERIA</div>
  <div class="pill" style="top:54px">Sed ut perspiciatis unde omnis iste natus error<span class="num">01</span></div>
  <div class="pill" style="top:91px">Ut enim ad minima veniam, quis n<span class="num">02</span></div>
  <div class="pill" style="top:129px">Sed ut perspiciatis unde omnis iste natus error<span class="num">03</span></div>
  <div class="pill" style="top:166px">Quis autem vel eum iure reprehenderit qui in ea volup<span class="num">04</span></div>
  <div class="pill" style="top:203px">Sed ut perspiciatis unde omnis iste natus error<span class="num">05</span></div>
</section>

<!-- Thank you -->
<section class="slide closing no-rule col-r row-4">
  <div class="scene" role="img" aria-label="Photo of a dim boardroom with people meeting beside tall windows at sunset"></div>
  <div class="panel">
    <h2>THANK YOU FOR YOUR TIME<br>AND ATTENTION.</h2>
    <p class="sub">We appreciate your engagement throughout this presentation.</p>
    <p class="txt">Thank you for your time and consideration. We appreciate the opportunity to present this analysis and share insights into the organization’s business approach, investment focus, and strategic positioning.</p>
    <p class="txt">We look forward to further discussions, addressing any questions, and exploring potential opportunities for collaboration in the future.</p>
  </div>
</section>

</body>
</html>
```